Career development coaching - school lever to adults, needs a business card

Tandem Lark - An independent Career Advice business that provides 1-2-1 advice,for career development, entrepreneurial support and workshops needs a business card. Our clients of all ages (school leaver to adults looking for a career move) and universities and colleges. We would like the card to be double-sided with a modern, professional look. Looking for something professional yet very creative and original. Want a standard size business card that inspires a second look because it stands out from the rest.

One side of the card to have a design incorporating the logo with Tandem Lark name with the strap line “Helping you find your future” and space for the company website

Other side of the card to the logo/Tandem Lark name and the usual contact information:
Individual Name
Job Title (for example, Director)
Phone number
Email address
Company website address

Facebook, LinkedIn and Twitter links will need to go somewhere (back or front!)

The design will be used for 3 individuals so should be editable so that we can update as needed/as we grow.

Attached is the company logo/colours to be incorporated.

Target Market(s)

1-2-1 advice,for career development, entrepreneurial support and workshops needs a business card. Our clients of all ages (school leaver to adults looking for a career move) and universities and colleges.

Industry/Entity Type

Consulting

Contact Information for Business Card

Individual Name
Phone number
Email address
Company website address

Font styles to use
Sans Serif

Colors
0255a3
3176b5
faa54b
f78f20
85acd3
cfdeed

Requirements
Must have
• use the Tandem Lark Logo in some way - using the colours and the blue/orange palette
• For the logo - hope this makes sense to someone or if they direclty relate to the logo image attached!
• For the Orange:- Pantone 1585 C
• In CMYK : C3 M71 Y100 K0
• For the Blue:- 100% Pantone 7469 C
• In CMYK : C100 M62 Y27 K7
• Please feel free to contact me with any questions for more info
Nice to have
• happy to see any creative designs
Should not have
• Nothing too traditional,

```html
<!DOCTYPE html>
<html lang="en">
<head>
<meta charset="utf-8">
<title>Tandem Lark – Business Card</title>
<link rel="stylesheet" href="https://fonts.googleapis.com/css2?family=Open+Sans:wght@400;600;700&display=swap">
<style>
  :root {
    --blue: #0f648c;
    --orange: #ee7535;
    --white: #ffffff;
    --backdrop: #e6e3df;
    --brand-blue: #0f648c;
  }
  * { margin: 0; padding: 0; box-sizing: border-box; }
  html, body {
    width: 1200px;
    height: 902px;
    overflow: hidden;
    background: var(--backdrop);
    font-family: "Open Sans", Arial, sans-serif;
  }
  .card {
    position: absolute;
    left: 100px;
    top: 166px;
    width: 1000px;
    height: 570px;
    border-radius: 22px;
    overflow: hidden;
    background: var(--white);
    box-shadow: 0 6px 24px rgba(0,0,0,0.15);
  }
  .card-shapes {
    position: absolute;
    inset: 0;
  }
  .name-badge {
    position: absolute;
    left: 0;
    top: 89px;
    width: 323px;
    height: 72px;
    background: var(--orange);
    border-radius: 0 4px 4px 0;
    color: var(--white);
    padding: 2px 0 0 52px;
  }
  .person-name {
    font-size: 32px;
    font-weight: 700;
    line-height: 38px;
    letter-spacing: 0.3px;
  }
  .job-title {
    font-size: 24px;
    font-weight: 600;
    line-height: 26px;
  }
  .address {
    position: absolute;
    left: 53px;
    top: 264px;
    color: var(--white);
    font-size: 26px;
    line-height: 35px;
  }
  .contact-list {
    position: absolute;
    left: 53px;
    top: 355px;
    list-style: none;
    color: var(--white);
    font-size: 26px;
    line-height: 32px;
  }
  .contact-item {
    display: flex;
    align-items: center;
    gap: 15px;
  }
  .contact-icon {
    width: 30px;
    height: 28px;
    flex: none;
  }
  .brand {
    position: absolute;
    left: 530px;
    width: 470px;
    top: 350px;
    display: flex;
    justify-content: center;
    align-items: center;
    gap: 14px;
  }
  .brand-dot {
    width: 22px;
    height: 22px;
    border-radius: 50%;
    background: var(--orange);
  }
  .brand-name {
    color: var(--brand-blue);
    font-size: 42px;
    font-weight: 600;
    letter-spacing: 1px;
  }
</style>
</head>
<body>
  <section class="card">
    <svg class="card-shapes" width="1000" height="570" viewBox="0 0 1000 570" aria-hidden="true">
      <path class="panel-blue" d="M0,0 H521 Q393,285 521,570 H0 Z" fill="var(--blue)"/>
      <path class="accent-crescent" d="M528,0 Q402,285 528,570 L533,570 Q426,285 533,0 Z" fill="var(--orange)"/>
    </svg>

    <div class="name-badge">
      <div class="person-name">NORA PELL</div>
      <div class="job-title">Maneger</div>
    </div>

    <p class="address">Harbor Lane, 2nd Ste<br>Millbrook, Avenshire 1234</p>

    <ul class="contact-list">
      <li class="contact-item">
        <svg class="contact-icon" viewBox="0 0 30 28" aria-hidden="true">
          <rect width="30" height="28" rx="3" fill="var(--orange)"/>
          <path d="M7 10 Q15 5 23 10 L21 13 L18 12 L18 10 Q15 9 12 10 L12 12 L9 13 Z" fill="var(--white)"/>
          <rect x="9" y="14" width="12" height="8" rx="1.5" fill="var(--white)"/>
        </svg>
        <span>555 014 2290</span>
      </li>
      <li class="contact-item">
        <svg class="contact-icon" viewBox="0 0 30 28" aria-hidden="true">
          <rect width="30" height="28" rx="3" fill="var(--orange)"/>
          <rect x="6" y="8" width="18" height="13" fill="var(--white)"/>
          <path d="M6 8 L15 16 L24 8 M6 21 L12 14 M24 21 L18 14" stroke="var(--orange)" stroke-width="1.5" fill="none"/>
        </svg>
        <span>hello@tandemlark.example</span>
      </li>
      <li class="contact-item">
        <svg class="contact-icon" viewBox="0 0 30 28" aria-hidden="true">
          <rect width="30" height="28" rx="3" fill="var(--orange)"/>
          <circle cx="15" cy="14" r="8.5" fill="none" stroke="var(--white)" stroke-width="1.6"/>
          <ellipse cx="15" cy="14" rx="3.5" ry="8.5" fill="none" stroke="var(--white)" stroke-width="1.4"/>
          <path d="M6.5 14 H23.5 M8 10 H22 M8 18 H22" stroke="var(--white)" stroke-width="1.3"/>
        </svg>
        <span>www.tandemlark.example</span>
      </li>
    </ul>

    <div class="brand">
      <span class="brand-dot"></span>
      <span class="brand-name">Tandem Lark</span>
    </div>
  </section>
</body>
</html>
```